Medical Research Web ad banners

We are a small independent Medical practice that conducts NRB pharmaceutical trials in Allergy, Asthma, and Rheumatology diseases. Our need is for 3 banner sizes to advertise for currently enrolling studies. Our Name is Quenby Research Center. We have a logo which I will attach (done through Pixel Huddle). We need the ad to say: Currently Enrolling Studies: (then list the following categories) Rheumatoid Arthritis, Asthma, Allergies, Lupus, COPD, Osteoarthritis. We do have a tag line which is: "Today's Question, Tomorrow's Answer" and a call to action statement: "Join Us in Finding the Answer" which can be used if you would like but we don't want to much "clutter" in the ads so they are easy to read and clicked on. The 3 sizes we are looking for are: Leader Board 728 x 90, Inline Rectangle 300 x 250, and Wide Skyscraper 160x 600.
Target Market(s)
Here is our website: www.quenbyresearch-example.com
We will be using these banners on Searchwick and TVK as well as some medical related sites to advertise for current studies. Our usual age audience is 18-85 year olds who have one of these diseases and are looking for a new or alternative treatment.
Industry/Entity Type
Pharmaceutical
Look and feel

```html
<!DOCTYPE html>
<html lang="en">
<head>
<meta charset="utf-8">
<title>Quenby Research Center – Currently Enrolling Studies</title>
<link rel="stylesheet" href="https://fonts.googleapis.com/css2?family=Tinos:wght@700&family=Arimo:wght@700&display=swap">
<style>
  :root {
    --navy: #1f3a6e;
    --green: #2b8a2b;
    --check: #3c9a22;
    --ink: #111111;
    --button: #1f7a2c;
    --button-edge: #145a1e;
    --paper: #ffffff;
  }
  html, body {
    margin: 0;
    padding: 0;
    overflow: hidden;
    background: var(--paper);
  }
  .banner {
    position: relative;
    width: 1200px;
    height: 148px;
    overflow: hidden;
    background: var(--paper);
    font-family: "Tinos", "Times New Roman", serif;
  }
  .brand {
    position: absolute;
    left: 10px;
    top: 14px;
    width: 180px;
    height: 120px;
    display: flex;
    flex-direction: column;
    align-items: center;
    justify-content: center;
    gap: 8px;
  }
  .brand-dot {
    width: 42px;
    height: 42px;
    border-radius: 50%;
    background: var(--navy);
  }
  .brand-name {
    margin: 0;
    color: var(--navy);
    font-weight: 700;
    font-size: 19px;
    line-height: 1.1;
    text-align: center;
  }
  .tagline {
    position: absolute;
    left: 230px;
    width: 840px;
    top: 0;
    margin: 0;
    text-align: center;
    color: var(--navy);
    font-weight: 700;
    font-size: 40px;
    line-height: 44px;
  }
  .call-to-action {
    position: absolute;
    left: 230px;
    width: 840px;
    top: 42px;
    margin: 0;
    text-align: center;
    color: var(--green);
    font-weight: 700;
    font-size: 33px;
    line-height: 40px;
  }
  .studies-label {
    position: absolute;
    left: 198px;
    width: 168px;
    top: 93px;
    margin: 0;
    text-align: center;
    color: var(--ink);
    font-weight: 700;
    font-size: 20px;
    line-height: 23px;
  }
  .study-list {
    list-style: none;
    margin: 0;
    padding: 0;
  }
  .study {
    position: absolute;
    display: flex;
    align-items: flex-end;
    gap: 4px;
    color: var(--ink);
    font-weight: 700;
    font-size: 19px;
    line-height: 22px;
    white-space: nowrap;
  }
  .study svg {
    width: 24px;
    height: 24px;
    flex: none;
  }
  .tick { fill: var(--check); }
  .enroll-button {
    position: absolute;
    left: 1033px;
    top: 54px;
    width: 157px;
    height: 42px;
    display: flex;
    align-items: center;
    justify-content: center;
    border-radius: 5px;
    background: var(--button);
    box-shadow: inset 0 -2px 0 var(--button-edge);
    color: #ffffff;
    font-family: "Arimo", Arial, sans-serif;
    font-weight: 700;
    font-size: 19px;
    text-decoration: none;
  }
</style>
</head>
<body>
<div class="banner">
  <div class="brand">
    <span class="brand-dot" aria-hidden="true"></span>
    <p class="brand-name">Quenby Research Center</p>
  </div>

  <h1 class="tagline">Today's Question, Tomorrow's Answer</h1>
  <p class="call-to-action">Join Us in Finding the Answer</p>

  <p class="studies-label">Currently Enrolling Studies</p>

  <ul class="study-list">
    <li class="study" style="left:446px; top:90px;"><svg viewBox="0 0 24 24" aria-hidden="true"><path class="tick" d="M2 13 L6 9 L10 14 L20 1 L23 4 L10 22 Z"/></svg>Rheumatoid Arthritis</li>
    <li class="study" style="left:446px; top:120px;"><svg viewBox="0 0 24 24" aria-hidden="true"><path class="tick" d="M2 13 L6 9 L10 14 L20 1 L23 4 L10 22 Z"/></svg>Asthma</li>
    <li class="study" style="left:682px; top:90px;"><svg viewBox="0 0 24 24" aria-hidden="true"><path class="tick" d="M2 13 L6 9 L10 14 L20 1 L23 4 L10 22 Z"/></svg>Allergies</li>
    <li class="study" style="left:682px; top:120px;"><svg viewBox="0 0 24 24" aria-hidden="true"><path class="tick" d="M2 13 L6 9 L10 14 L20 1 L23 4 L10 22 Z"/></svg>Lupus</li>
    <li class="study" style="left:827px; top:90px;"><svg viewBox="0 0 24 24" aria-hidden="true"><path class="tick" d="M2 13 L6 9 L10 14 L20 1 L23 4 L10 22 Z"/></svg>COPD</li>
    <li class="study" style="left:827px; top:120px;"><svg viewBox="0 0 24 24" aria-hidden="true"><path class="tick" d="M2 13 L6 9 L10 14 L20 1 L23 4 L10 22 Z"/></svg>Osteoarthritis</li>
  </ul>

  <a class="enroll-button" href="https://www.quenbyresearch-example.com">Enroll Today</a>
</div>
</body>
</html>
```